Personal Finance Blog Wordpress Design

We are looking for a new Wordpress theme design for CoinHarbor.com.

All of the elements that are currently on the homepage should remain, minus the archives list. The placement of various elements can be changed, we just need a more modern and clean feel. We would like to add a 160 x 600 ad unit on the homepage. We would like the 728x90 ad to be below the navigation similar to that of: http://www.plumtreeledger.example/blog/

We like the fonts used on: http://www.quillpocket.example/blog/

The text that currently resides at the bottom of CoinHarbor.com needs to remain on the homepage, but wherever it is placed needs to not be intrusive.

The color scheme needs to appropriately compliment the logo.

No sliders. I don't like sliders.

I am happy to answer questions.

Industry/Entity Type

Finance

Requirements
Must have
• Included in project description
Nice to have
Should not have
• Included in project description. Don't use sliders

```html
<!DOCTYPE html>
<html lang="en">
<head>
<meta charset="utf-8">
<title>CoinHarbor – Personal Finance Blog</title>
<link href="https://fonts.googleapis.com/css2?family=Raleway:wght@400;500;600;700;800&display=swap" rel="stylesheet">
<style>
:root{
  --green-dark:#2f6a2c;
  --green:#7dbf3b;
  --green-soft:#8cc63f;
  --orange:#f7941d;
  --red:#e23b2e;
  --ink:#2b2b2b;
  --muted:#8a8a8a;
  --line:#e3e3e3;
  --panel:#f3f3f3;
  --charcoal:#333333;
}
*{box-sizing:border-box}
html,body{margin:0;padding:0}
body{width:1200px;height:3982px;overflow:hidden;position:relative;background:#fff;color:var(--ink);font-family:'Raleway',sans-serif}
a{color:inherit;text-decoration:none}
ul{list-style:none;margin:0;padding:0}
h3{margin:0}

.topbar{position:absolute;left:0;top:0;width:1200px;height:21px;background:var(--green);color:#fff;font-size:10px;display:flex;align-items:center;justify-content:space-between;padding:0 93px;white-space:nowrap}
.topbar nav a{margin-right:14px}
.topbar .dots{display:flex;gap:6px}
.topbar .dots i{width:9px;height:9px;border-radius:50%;background:#fff;display:block}

.brand{position:absolute;left:0;top:34px;width:1200px;text-align:center}
.brand .mark{display:block;width:44px;height:44px;border-radius:50%;background:var(--green-dark);margin:0 auto 6px}
.brand .name{font-size:30px;font-weight:800;color:var(--green-dark);letter-spacing:-.3px}

.mainnav{position:absolute;left:0;top:138px;width:1200px;height:37px;background:var(--green-dark);padding:0 90px;display:flex;align-items:stretch;justify-content:space-between}
.mainnav a{color:#fff;font-size:12px;font-weight:500;padding:0 10px;display:flex;align-items:center;white-space:nowrap}
.mainnav a.active{background:var(--green)}

.ad-leader{position:absolute;left:191px;top:212px;width:552px;height:59px;background:#3a3a3a;color:#bbb;font-size:22px;letter-spacing:1px;display:flex;align-items:center;justify-content:center}

.feature{position:absolute;left:93px;top:297px;width:770px}
.feature .media{height:353px;background:linear-gradient(135deg,#c9c2b8,#8e8a84 55%,#5b5a58)}
.tag{position:absolute;left:0;top:0;background:var(--green);color:#fff;font-size:12px;padding:5px 10px;display:flex;align-items:center;gap:6px}
.tag.orange{left:0;top:58px;background:var(--orange);font-size:13px;padding:8px 14px}
.tag svg{width:12px;height:12px}
.card-media,.feature .media{position:relative}
.head{display:flex;align-items:center;justify-content:space-between;height:52px}
.head h3{font-size:17px;font-weight:700;white-space:nowrap;overflow:hidden}
.feature .head h3{font-size:20px}
.go{flex:0 0 26px;width:26px;height:26px;border-radius:50%;background:var(--green-dark);display:flex;align-items:center;justify-content:center}
.go svg{width:10px;height:10px}
.meta-bar{height:35px;background:var(--green);color:#fff;font-size:11px;font-weight:600;display:flex;align-items:center;justify-content:space-between;padding:0 10px}
.stats{display:flex;gap:10px;align-items:center}
.stats span{display:flex;align-items:center;gap:4px}
.stats svg{width:13px;height:13px}

.card{position:absolute;width:370px}
.card-media{height:279px}
.mini-list{margin-top:14px}
.mini-list li{display:flex;gap:12px;height:70px;margin-bottom:10px}
.thumb{flex:0 0 56px;height:46px}
.mini-list h4{margin:0 0 6px;font-size:13px;font-weight:500;line-height:1.3}
.mini-meta{font-size:10px;color:var(--muted);display:flex;gap:10px}
.mini-meta span{display:flex;align-items:center;gap:3px}
.mini-meta svg{width:11px;height:11px}
.btn{display:inline-block;background:var(--green-dark);color:#fff;font-size:11px;font-weight:600;padding:8px 14px}

.rule{position:absolute;left:93px;width:770px;height:1px;background:var(--line)}

.updates-bar{position:absolute;left:93px;top:2010px;width:770px;height:48px;background:var(--charcoal);color:#fff;font-size:20px;font-weight:600;display:flex;align-items:center;gap:12px;padding:0 14px}
.updates-bar svg{width:22px;height:22px}
.update{position:absolute;top:2076px;width:248px;background:#f4f4f4}
.update .u-media{height:149px;position:relative}
.update .u-meta{position:absolute;left:0;bottom:0;right:0;height:24px;background:var(--green);color:#fff;font-size:9px;display:flex;align-items:center;gap:8px;padding:0 8px}
.update h4{margin:0;padding:22px 10px 4px;font-size:13px;font-weight:500;line-height:1.3}
.update .u-cat{font-size:10px;color:var(--muted);padding:0 10px 14px}
.update .plus{position:absolute;right:0;bottom:0;width:26px;height:26px;background:var(--green);color:#fff;font-size:18px;display:flex;align-items:center;justify-content:center}

.side{position:absolute;left:889px;width:221px}
.w-title{height:34px;background:var(--green-dark);color:#fff;font-size:14px;font-weight:700;display:flex;align-items:center;padding:0 12px}
.search{display:flex;margin-top:20px}
.search input{flex:1;min-width:0;height:26px;border:1px solid var(--line);font:10px 'Raleway',sans-serif;padding:0 8px}
.search button{background:var(--orange);color:#fff;border:0;font:600 10px 'Raleway',sans-serif;padding:0 14px}
.socials{display:flex;justify-content:space-between;padding:16px 6px 0}
.socials div{text-align:center;font-size:9px;color:var(--muted)}
.socials i{display:block;width:40px;height:40px;border-radius:50%;margin:0 auto 4px}
.latest li{display:flex;gap:10px;height:66px;padding-top:10px}
.latest .dot{flex:0 0 40px;height:40px;border-radius:50%;background:#d9e8cf}
.latest h4{margin:0 0 4px;font-size:11px;font-weight:600;line-height:1.3}
.latest .mini-meta{font-size:8px}
.ad-sky{margin:48px auto 0;width:125px;height:470px;background:#3a3a3a;color:#aaa;font-size:17px;letter-spacing:2px;line-height:2.4;display:flex;align-items:center;justify-content:center;text-align:center}
.box{border:1px solid var(--line);padding:10px}
.box-title{font-size:10px;font-weight:700;color:var(--green-dark);display:flex;justify-content:space-between;align-items:center;border-bottom:1px solid var(--line);padding-bottom:8px}
.box-title i{width:16px;height:16px;display:block}
.fb-grid{display:grid;grid-template-columns:repeat(5,1fr);gap:5px;margin-top:8px}
.fb-grid span{height:30px;background:#c7cdd6}
.newsletter{text-align:center;padding-top:10px}
.newsletter h5{margin:0;font-size:18px;font-weight:600}
.newsletter p{margin:8px 20px;font-size:9px;color:var(--muted);line-height:1.4}
.newsletter .row{display:flex;margin:0 14px}
.newsletter .row span{flex:1;height:22px;border:1px solid var(--line);font-size:8px;color:var(--muted);text-align:left;padding:6px}
.newsletter .row b{background:var(--orange);color:#fff;font-size:9px;padding:6px 8px;font-weight:600}
.tweet{display:flex;gap:8px;margin-top:10px;font-size:8px;line-height:1.4;color:#555}
.tweet .av{flex:0 0 34px;height:34px;background:var(--green-soft)}
.tweet b{color:var(--green-dark)}
.cats li{height:29px;border-bottom:1px solid var(--line);font-size:11px;display:flex;align-items:center;padding-left:14px}
.tags{display:flex;flex-wrap:wrap;gap:6px 10px;font-size:10px;padding:10px 6px}
.tags span.on{background:var(--green-dark);color:#fff;padding:3px 6px}

.about{position:absolute;left:0;top:3637px;width:1200px;height:293px;background:var(--panel)}
.about h2{position:absolute;left:109px;top:30px;margin:0;font-size:28px;font-weight:700;color:var(--green)}
.about p{position:absolute;left:109px;top:78px;width:590px;margin:0;font-size:13px;line-height:1.45;color:#444}
.about .btn{position:absolute;left:109px;top:220px}
.about .screen{position:absolute;left:805px;top:20px;width:300px;height:240px}
.foot{position:absolute;left:0;top:3948px;width:1200px;height:34px;background:var(--green);color:#fff;font-size:10px;display:flex;align-items:center;justify-content:space-between;padding:0 93px}
.foot nav a{margin-left:14px}
</style>
</head>
<body>
<svg width="0" height="0" style="position:absolute">
  <defs>
    <symbol id="i-eye" viewBox="0 0 16 16"><path d="M1 8s2.5-5 7-5 7 5 7 5-2.5 5-7 5-7-5-7-5z" fill="none" stroke="currentColor" stroke-width="1.5"/><circle cx="8" cy="8" r="2.2" fill="currentColor"/></symbol>
    <symbol id="i-chat" viewBox="0 0 16 16"><path d="M2 3h12v8H7l-3 3v-3H2z" fill="currentColor"/></symbol>
    <symbol id="i-share" viewBox="0 0 16 16"><circle cx="12" cy="3.5" r="2" fill="currentColor"/><circle cx="4" cy="8" r="2" fill="currentColor"/><circle cx="12" cy="12.5" r="2" fill="currentColor"/><path d="M12 3.5L4 8l8 4.5" stroke="currentColor" stroke-width="1.3" fill="none"/></symbol>
    <symbol id="i-arrow" viewBox="0 0 10 10"><path d="M3 1l4 4-4 4" stroke="#fff" stroke-width="2" fill="none"/></symbol>
    <symbol id="i-folder" viewBox="0 0 16 16"><path d="M1 3h5l2 2h7v9H1z" fill="none" stroke="currentColor" stroke-width="1.5"/></symbol>
  </defs>
</svg>

<header>
  <div class="topbar">
    <nav><a>Wednesday, 08 April 2015</a><a>Advertisement</a><a>Dropdown</a><a>Page / Post Elements</a><a>Forums</a><a>Contact us</a></nav>
    <div class="dots"><i></i><i></i><i></i><i></i><i></i></div>
  </div>
  <div class="brand"><span class="mark"></span><span class="name">CoinHarbor</span></div>
  <nav class="mainnav">
    <a class="active">Home</a><a>Auto</a><a>Bank Accounts ▾</a><a>Credit Cards</a><a>Insurance</a><a>Investments ▾</a><a>Mortgages</a><a>Personal Finance</a><a>Small Business</a><a>Taxes Others</a>
  </nav>
</header>

<div class="ad-leader">AD SPACE 728x90</div>

<main>
  <section class="feature">
    <div class="media" role="img" aria-label="Photo of hands using a tablet to browse furniture in a living room"><span class="tag orange">Featured Post</span></div>
    <div class="head"><h3>Why You Should Buy Furniture Online</h3><span class="go"><svg><use href="#i-arrow"/></svg></span></div>
    <div class="meta-bar"><span>April 28, 2015</span><span class="stats"><span><svg><use href="#i-eye"/></svg>328</span><span><svg><use href="#i-chat"/></svg>12</span><span><svg><use href="#i-share"/></svg>128</span></span></div>
  </section>

  <article class="card" style="left:101px;top:770px">
    <div class="card-media" role="img" aria-label="Photo of cars in a parking lot with a fuel gauge" style="background:linear-gradient(135deg,#9ea4a8,#5f666b)"><span class="tag"><svg><use href="#i-folder"/></svg>Auto</span></div>
    <div class="head"><h3>7 Cars With Good Gas Mileage</h3><span class="go"><svg><use href="#i-arrow"/></svg></span></div>
    <div class="meta-bar"><span>April 28, 2015</span><span class="stats"><span><svg><use href="#i-eye"/></svg>328</span><span><svg><use href="#i-chat"/></svg>12</span><span><svg><use href="#i-share"/></svg>128</span></span></div>
    <ul class="mini-list">
      <li><span class="thumb" role="img" aria-label="Photo of a car on a road" style="background:#a7b1b7"></span><div><h4>Can You Get a Car Loan with Bad Credit?</h4><div class="mini-meta"><span>April 28, 2015</span><span><svg><use href="#i-eye"/></svg>328</span><span><svg><use href="#i-chat"/></svg>12</span></div></div></li>
      <li><span class="thumb" role="img" aria-label="Illustration of a balance scale" style="background:#4f7a3a"></span><div><h4>Leasing vs. Buying a Car: Comparing Present to Future Costs ?</h4><div class="mini-meta"><span>April 28, 2015</span><span><svg><use href="#i-eye"/></svg>640</span><span><svg><use href="#i-chat"/></svg>128</span></div></div></li>
    </ul>
    <a class="btn">Load More</a>
  </article>
  <article class="card" style="left:491px;top:770px">
    <div class="card-media" role="img" aria-label="Illustration of rising stacks of banknotes with a red arrow" style="background:linear-gradient(160deg,#ffffff,#d8d8d0 60%,#9aa08a)"><span class="tag"><svg><use href="#i-folder"/></svg>Bank Accounts</span></div>
    <div class="head"><h3>Want to Increase Your Savings?</h3><span class="go"><svg><use href="#i-arrow"/></svg></span></div>
    <div class="meta-bar"><span>April 28, 2015</span><span class="stats"><span><svg><use href="#i-eye"/></svg>328</span><span><svg><use href="#i-chat"/></svg>12</span><span><svg><use href="#i-share"/></svg>128</span></span></div>
    <ul class="mini-list">
      <li><span class="thumb" role="img" aria-label="Photo of a car" style="background:#b7a892"></span><div><h4>Can You Get a Car Loan with Bad Credit?</h4><div class="mini-meta"><span>April 28, 2015</span><span><svg><use href="#i-eye"/></svg>328</span><span><svg><use href="#i-chat"/></svg>12</span></div></div></li>
      <li><span class="thumb" role="img" aria-label="Illustration of a balance scale" style="background:#4f7a3a"></span><div><h4>Leasing vs. Buying a Car: Comparing Present to Future Costs ?</h4><div class="mini-meta"><span>April 28, 2015</span><span><svg><use href="#i-eye"/></svg>640</span><span><svg><use href="#i-chat"/></svg>128</span></div></div></li>
    </ul>
    <a class="btn">Load More</a>
  </article>

  <div class="rule" style="top:1375px"></div>

  <article class="card" style="left:101px;top:1407px">
    <div class="card-media" role="img" aria-label="Photo of a brushed metal card-brand sign" style="background:linear-gradient(135deg,#b9b6b1,#7e7b77)"><span class="tag"><svg><use href="#i-folder"/></svg>Credit Cards</span></div>
    <div class="head"><h3>Benefits of a Meridian It Card</h3><span class="go"><svg><use href="#i-arrow"/></svg></span></div>
    <div class="meta-bar"><span>April 28, 2015</span><span class="stats"><span><svg><use href="#i-eye"/></svg>1026</span><span><svg><use href="#i-chat"/></svg>147</span><span><svg><use href="#i-share"/></svg>128</span></span></div>
    <ul class="mini-list">
      <li><span class="thumb" role="img" aria-label="Photo of a student" style="background:#c79b7d"></span><div><h4>Credit Tips for Students: How Do Credit Cards Work?</h4><div class="mini-meta"><span>April 28, 2015</span><span><svg><use href="#i-eye"/></svg>640</span><span><svg><use href="#i-chat"/></svg>128</span></div></div></li>
      <li><span class="thumb" role="img" aria-label="Photo of a metal card sign" style="background:#9c9994"></span><div><h4>How Do I Qualify for a Meridian Student Card?</h4><div class="mini-meta"><span>April 28, 2015</span><span><svg><use href="#i-eye"/></svg>640</span><span><svg><use href="#i-chat"/></svg>128</span></div></div></li>
    </ul>
    <a class="btn">Load More</a>
  </article>
  <article class="card" style="left:491px;top:1407px">
    <div class="card-media" role="img" aria-label="Photo of a dental checkup" style="background:linear-gradient(135deg,#cfdfe6,#7fa0b3)"><span class="tag"><svg><use href="#i-folder"/></svg>Insurance</span></div>
    <div class="head"><h3>What is the Best Dental Insurance ....</h3><span class="go"><svg><use href="#i-arrow"/></svg></span></div>
    <div class="meta-bar"><span>April 28, 2015</span><span class="stats"><span><svg><use href="#i-eye"/></svg>328</span><span><svg><use href="#i-chat"/></svg>12</span><span><svg><use href="#i-share"/></svg>128</span></span></div>
    <ul class="mini-list">
      <li><span class="thumb" role="img" aria-label="Photo of a car key" style="background:#8d9aa3"></span><div><h4>Five Ways to Obtain Affordable Car Insurance</h4><div class="mini-meta"><span>April 28, 2015</span><span><svg><use href="#i-eye"/></svg>640</span><span><svg><use href="#i-chat"/></svg>128</span></div></div></li>
      <li><span class="thumb" role="img" aria-label="Photo of insurance paperwork" style="background:#c9b58c"></span><div><h4>How to Protect Yourself From Insurance Fraud ?</h4><div class="mini-meta"><span>April 28, 2015</span><span><svg><use href="#i-eye"/></svg>640</span><span><svg><use href="#i-chat"/></svg>128</span></div></div></li>
    </ul>
    <a class="btn">Load More</a>
  </article>

  <div class="updates-bar"><svg><use href="#i-folder"/></svg>Latest Updates</div>
  <div class="update" style="left:101px">
    <div class="u-media" role="img" aria-label="Radio company sign" style="background:linear-gradient(135deg,#1f4f9a,#0b2a5c)"><div class="u-meta"><span>April 28, 2015</span><span>328</span><span>12</span><span>128</span></div></div>
    <h4>Orbitwave Radio Stock: How it Fares in 2015</h4><div class="u-cat">Investment</div><span class="plus">+</span>
  </div>
  <div class="update" style="left:357px">
    <div class="u-media" role="img" aria-label="Photo of a brick house" style="background:linear-gradient(160deg,#c9d6e0,#8a5a44)"></div>
    <h4>Financial Benefits of Buying Fore closed Homes</h4><div class="u-cat">Mortgages</div><span class="plus">+</span>
  </div>
  <div class="update" style="left:613px">
    <div class="u-media" role="img" aria-label="Photo of a shopper in an appliance store" style="background:linear-gradient(135deg,#d8d2c6,#8f877a)"></div>
    <h4>5 Appliances on Sale to Save Money</h4><div class="u-cat">Personal Finance</div><span class="plus">+</span>
  </div>

  <div class="rule" style="top:2363px"></div>

  <article class="card" style="left:101px;top:2390px">
    <div class="card-media" role="img" aria-label="Corporate sign in blue" style="background:linear-gradient(135deg,#3b62b0,#1c3c86)"><span class="tag"><svg><use href="#i-folder"/></svg>Investments</span></div>
    <div class="head"><h3>Are 2015 Generon Stock Prices ..</h3><span class="go"><svg><use href="#i-arrow"/></svg></span></div>
    <div class="meta-bar"><span>April 28, 2015</span><span class="stats"><span><svg><use href="#i-eye"/></svg>328</span><span><svg><use href="#i-chat"/></svg>12</span><span><svg><use href="#i-share"/></svg>128</span></span></div>
    <ul class="mini-list">
      <li><span class="thumb" role="img" aria-label="Photo of a financial chart" style="background:#6a7176"></span><div><h4>Average Retirement Savings Needed to Retire</h4><div class="mini-meta"><span>April 28, 2015</span><span><svg><use href="#i-eye"/></svg>640</span><span><svg><use href="#i-chat"/></svg>128</span></div></div></li>
      <li><span class="thumb" role="img" aria-label="Illustration of a balance scale" style="background:#4f7a3a"></span><div><h4>Leasing vs. Buying a Car: Comparing Present to Future Costs ?</h4><div class="mini-meta"><span>April 28, 2015</span><span><svg><use href="#i-eye"/></svg>640</span><span><svg><use href="#i-chat"/></svg>128</span></div></div></li>
    </ul>
    <a class="btn">Load More</a>
  </article>
  <article class="card" style="left:491px;top:2390px">
    <div class="card-media" role="img" aria-label="Photo of a model house beside a calculator" style="background:linear-gradient(160deg,#f1f1f1,#b8b8b8)"><span class="tag"><svg><use href="#i-folder"/></svg>Mortgages</span></div>
    <div class="head"><h3>Moving on Up: What Mortgage Can .....</h3><span class="go"><svg><use href="#i-arrow"/></svg></span></div>
    <div class="meta-bar"><span>April 28, 2015</span><span class="stats"><span><svg><use href="#i-eye"/></svg>328</span><span><svg><use href="#i-chat"/></svg>12</span><span><svg><use href="#i-share"/></svg>128</span></span></div>
    <ul class="mini-list">
      <li><span class="thumb" role="img" aria-label="Photo of a house" style="background:#b39b7f"></span><div><h4>What Are the Pros and Cons of 10 Year Mortgage Rates?</h4><div class="mini-meta"><span>April 28, 2015</span><span><svg><use href="#i-eye"/></svg>640</span><span><svg><use href="#i-chat"/></svg>128</span></div></div></li>
      <li><span class="thumb" role="img" aria-label="Photo of a brick house" style="background:#8a5a44"></span><div><h4>Financial Benefits of Buying Foreclosed Homes</h4><div class="mini-meta"><span>April 28, 2015</span><span><svg><use href="#i-eye"/></svg>640</span><span><svg><use href="#i-chat"/></svg>128</span></div></div></li>
    </ul>
    <a class="btn">Load More</a>
  </article>

  <div class="rule" style="top:2995px"></div>

  <article class="card" style="left:101px;top:3027px">
    <div class="card-media" role="img" aria-label="Photo of a hand holding a remote toward a television" style="background:linear-gradient(135deg,#7d8f9e,#2e3a44)"><span class="tag"><svg><use href="#i-folder"/></svg>Personal Finance</span></div>
    <div class="head"><h3>Are Cable Packages Really a Good Deal</h3><span class="go"><svg><use href="#i-arrow"/></svg></span></div>
    <div class="meta-bar"><span>April 28, 2015</span><span class="stats"><span><svg><use href="#i-eye"/></svg>328</span><span><svg><use href="#i-chat"/></svg>12</span><span><svg><use href="#i-share"/></svg>128</span></span></div>
    <ul class="mini-list">
      <li><span class="thumb" role="img" aria-label="Photo of a student" style="background:#c79b7d"></span><div><h4>Credit Tips for Students: How Do Credit Cards Work?</h4><div class="mini-meta"><span>April 28, 2015</span><span><svg><use href="#i-eye"/></svg>640</span><span><svg><use href="#i-chat"/></svg>128</span></div></div></li>
      <li><span class="thumb" role="img" aria-label="Photo of a metal card sign" style="background:#9c9994"></span><div><h4>How Do I Qualify for a Meridian Student Card?</h4><div class="mini-meta"><span>April 28, 2015</span><span><svg><use href="#i-eye"/></svg>640</span><span><svg><use href="#i-chat"/></svg>128</span></div></div></li>
    </ul>
    <a class="btn">Load More</a>
  </article>
  <article class="card" style="left:491px;top:3027px">
    <div class="card-media" role="img" aria-label="Photo of a relaxed office worker at a desk" style="background:linear-gradient(135deg,#e0e0dc,#8d8f8a)"><span class="tag"><svg><use href="#i-folder"/></svg>Small Business</span></div>
    <div class="head"><h3>Best Budgeting Software for 2015</h3><span class="go"><svg><use href="#i-arrow"/></svg></span></div>
    <div class="meta-bar"><span>April 28, 2015</span><span class="stats"><span><svg><use href="#i-eye"/></svg>328</span><span><svg><use href="#i-chat"/></svg>12</span><span><svg><use href="#i-share"/></svg>128</span></span></div>
    <ul class="mini-list">
      <li><span class="thumb" role="img" aria-label="Photo of business receipts" style="background:#c2b79a"></span><div><h4>How Do You Know If Your Business Expenses Are Too High?</h4><div class="mini-meta"><span>April 28, 2015</span><span><svg><use href="#i-eye"/></svg>640</span><span><svg><use href="#i-chat"/></svg>128</span></div></div></li>
      <li><span class="thumb" role="img" aria-label="Photo of insurance paperwork" style="background:#c9b58c"></span><div><h4>How to Protect Yourself From Insurance Fraud ?</h4><div class="mini-meta"><span>April 28, 2015</span><span><svg><use href="#i-eye"/></svg>640</span><span><svg><use href="#i-chat"/></svg>128</span></div></div></li>
    </ul>
    <a class="btn">Load More</a>
  </article>
</main>

<aside>
  <div class="side" style="top:199px">
    <div class="w-title">Search Bar</div>
    <div class="search"><input placeholder="Type and hit enter here"><button>SEARCH</button></div>
  </div>
  <div class="side" style="top:300px">
    <div class="w-title">We Are Social</div>
    <div class="socials">
      <div><i style="background:#3b5998"></i>70<br>Fans</div>
      <div><i style="background:#29a9e1"></i>64<br>Followers</div>
      <div><i style="background:#1c87bd"></i>80<br>Followers</div>
      <div><i style="background:#f58b1f"></i>64<br>Subscribers</div>
    </div>
  </div>
  <div class="side" style="top:433px">
    <div class="w-title">Latest Post</div>
    <ul class="latest">
      <li><span class="dot"></span><div><h4>Can You Get a Car Loan with Bad Credit?</h4><div class="mini-meta"><span>April 28, 2015</span><span>640</span><span>128</span></div></div></li>
      <li><span class="dot"></span><div><h4>Leasing vs. Buying a Car: Comparing Present ?</h4><div class="mini-meta"><span>April 28, 2015</span><span>640</span><span>128</span></div></div></li>
      <li><span class="dot"></span><div><h4>Can You Get a Car Loan with Bad Credit?</h4><div class="mini-meta"><span>April 28, 2015</span><span>640</span><span>128</span></div></div></li>
      <li><span class="dot"></span><div><h4>Leasing vs. Buying a Car: Comparing Present ?</h4><div class="mini-meta"><span>April 28, 2015</span><span>640</span><span>128</span></div></div></li>
      <li><span class="dot"></span><div><h4>Can You Get a Car Loan with Bad Credit?</h4><div class="mini-meta"><span>April 28, 2015</span><span>640</span><span>128</span></div></div></li>
    </ul>
  </div>
  <div class="side" style="top:828px">
    <div class="w-title">Advertisement</div>
    <div class="ad-sky">AD<br>SPACE<br>160x600</div>
  </div>
  <div class="side box" style="top:1399px;height:247px">
    <div class="box-title">LIKE US ON CIRCLEBOOK <i style="background:#3b5998"></i></div>
    <div style="display:flex;gap:8px;margin-top:8px;font-size:9px"><span style="width:30px;height:30px;background:var(--green-soft)"></span><span><b>CoinHarbor</b><br>Like page</span></div>
    <div style="font-size:8px;color:var(--muted);margin-top:8px">342 people like CoinHarbor</div>
    <div class="fb-grid"><span></span><span></span><span></span><span></span><span></span><span></span><span></span><span></span><span></span><span></span></div>
    <div style="font-size:8px;color:var(--muted);margin-top:8px">Circlebook social plugin</div>
  </div>
  <div class="side newsletter" style="top:1660px">
    <h5>Newsletter</h5>
    <p>Sign up here to receive breaking news and stories sent right to your inbox.</p>
    <div class="row"><span>Enter your email</span><b>Subscribe</b></div>
  </div>
  <div class="side" style="top:1792px">
    <div class="w-title">Advertisement</div>
    <div role="img" aria-label="Photo of a wooden pier with space for ads text" style="margin-top:18px;height:199px;background:linear-gradient(180deg,#6d7478,#2f3336);color:#fff;font-size:12px;font-weight:700;display:flex;align-items:center;justify-content:center;letter-spacing:1px">SPACE FOR ADS</div>
  </div>
  <div class="side box" style="top:2079px;height:226px">
    <div class="box-title">FOLLOW US CHIRPER <i style="background:#29a9e1;border-radius:50%"></i></div>
    <div class="tweet"><span class="av"></span><div><b>CoinHarbor · Nov 12</b><br>Fresh ideas for saving money this month, read the new guide on our blog today</div></div>
    <div class="tweet"><span class="av"></span><div><b>CoinHarbor · Nov 12</b><br>Fresh ideas for saving money this month, read the new guide on our blog today</div></div>
    <div class="tweet"><span class="av"></span><div><b>CoinHarbor · Nov 12</b><br>Fresh ideas for saving money this month, read the new guide on our blog today</div></div>
  </div>
  <div class="side" style="top:2350px">
    <div class="w-title">Categories</div>
    <ul class="cats" style="margin-top:8px">
      <li>Home</li><li>Auto</li><li>Bank Accounts</li><li>Credit Cards</li><li>Insurance</li><li>Investments</li><li>Mortgages</li><li>Personal Finance</li><li>Small Business</li><li>Taxes</li><li>Other</li>
    </ul>
  </div>
  <div class="side box" style="top:2795px;height:240px">
    <div class="box-title" style="color:var(--red)">SUBSCRIBE OUR CHANNEL <i style="background:var(--red)"></i></div>
    <div role="img" aria-label="Video still of a business meeting" style="margin:10px auto 0;width:170px;height:120px;background:linear-gradient(135deg,#5a6b78,#2b3540)"></div>
    <div style="margin:10px auto 0;width:130px;background:var(--red);color:#fff;font-size:10px;font-weight:700;text-align:center;padding:7px">SUBSCRIBE NOW</div>
  </div>
  <div class="side" style="top:3066px">
    <div role="img" aria-label="Photo of a laptop workspace with a news teaser" style="height:213px;background:linear-gradient(180deg,#3f4a52,#1d2328);color:#fff;font-size:10px;padding:10px">
      <span style="background:var(--green);padding:2px 5px;font-size:8px">CHANNEL NEWS</span>
      <p style="margin:8px 0 0;line-height:1.4">Lorem ipsum dolor sit amet, now in stock since today.</p>
    </div>
  </div>
  <div class="side" style="top:3320px">
    <div style="font-size:18px;font-weight:600;text-align:center">Tags Cloud</div>
    <div class="tags"><span class="on">Business</span><span>Finance</span><span>Online Banking</span><span>Insurance</span><span>Auto</span><span>Investment</span><span>Medical</span><span>Expenses</span><span>Software</span><span>Rent</span></div>
  </div>
</aside>

<section class="about">
  <h2>CoinHarbor Personal Finance Blog</h2>
  <p>Our mission is to enrich the lives of our readers (literally) by providing the very best personal finance content on the internet. Our readers may be at different stages in life, with different personal finance situations and needs: One person may be looking to get their first credit card, another might be looking into how to get a mortgage to buy a home, some may be looking for ways to afford or finance a college education for themselves or their children, many want to know how to improve their credit score, and still others.</p>
  <a class="btn">Read More</a>
  <div class="screen" role="img" aria-label="Desktop monitor showing the blog homepage" style="background:linear-gradient(160deg,#f5f5f5,#c9d3c4);border:10px solid #222;border-radius:6px"></div>
</section>
<footer class="foot">
  <span>© 2015 CoinHarbor. All rights reserved.</span>
  <nav><a>Terms &amp; Condition</a><a>Privacy Policy</a><a>Contact Us</a></nav>
</footer>
</body>
</html>
```